Cleaners Needs Bounce-Back Coupon For Laundry Service

We need a "bounce-back" coupon to attach to peoples dry cleaning orders that offers one free wash-n-fold laundry service. Right now we always attach their receipt to the bag that contains their dry cleaning when we return it. We'd like to also attach a coupon that will entice them to come try our laundry service.

Background on the service: We sort, wash, dry, and fold the laundry for customers and then neatly put it in a nice bag that makes returning very convenient. Their laundry comes out fresh, clean, smelling great, and without the hassle of doing it themselves. We have a great return rate. Most customers that try out the service become long term customers. The goal is to get our dry cleaning customers to come try it out.

Requirements:
* 5" x 8" and one-sided.
* To be printed on a standard color of card stock.
* Must incorporate our logo.
* Needs a place for us to fill in an expiration date. We'll fill in a date about two weeks out from the time they pick up their dry cleaning.
* Limit one coupon per customer.
* Limit 50 pounds of laundry per coupon.

```html
<!DOCTYPE html>
<html lang="en">
<head>
<meta charset="utf-8">
<title>Suds on Seventh – Free Wash-n-Fold Coupon</title>
<link href="https://fonts.googleapis.com/css2?family=Chewy&family=Open+Sans:wght@700;800&display=swap" rel="stylesheet">
<style>
  :root {
    --orange: #f26b21;
    --blue-dark: #1f4e9e;
    --blue-mid: #2f6fc0;
    --blue-light: #bcd6ef;
    --blue-pale: #e4eff9;
    --white: #ffffff;
    --line-grey: #9aa3ad;
  }
  html, body {
    margin: 0;
    padding: 0;
    overflow: hidden;
    background: #ffffff;
  }
  .coupon {
    position: relative;
    width: 1200px;
    height: 750px;
    background: var(--orange);
    overflow: hidden;
    font-family: "Open Sans", Arial, sans-serif;
    color: var(--white);
  }
  .coupon__backdrop {
    position: absolute;
    inset: 0;
  }
  .website {
    position: absolute;
    left: 40px;
    top: 32px;
    font-weight: 800;
    font-size: 22px;
    letter-spacing: 0.2px;
  }
  .brand {
    position: absolute;
    left: 720px;
    top: 58px;
    display: flex;
    align-items: center;
    gap: 18px;
  }
  .brand__mark {
    width: 64px;
    height: 64px;
    background: var(--white);
    border-radius: 8px;
  }
  .brand__name {
    font-weight: 800;
    font-size: 50px;
    line-height: 1;
    color: var(--white);
  }
  .contact {
    position: absolute;
    right: 45px;
    top: 190px;
    text-align: right;
    font-weight: 800;
    font-size: 23px;
    line-height: 1.32;
  }
  .contact__phone {
    font-size: 28px;
    display: inline-flex;
    align-items: center;
    gap: 8px;
  }
  .contact__phone svg { width: 26px; height: 26px; }
  .washer-door {
    position: absolute;
    left: 0;
    top: 0;
  }
  .offer {
    position: absolute;
    left: 110px;
    top: 290px;
    width: 560px;
    text-align: center;
    font-family: "Chewy", "Comic Sans MS", cursive;
    line-height: 0.9;
  }
  .offer__line { display: block; }
  .offer__one { font-size: 118px; color: var(--orange); }
  .offer__free { font-size: 108px; color: var(--orange); letter-spacing: 2px; }
  .offer__service-name { font-size: 86px; color: var(--blue-dark); margin-top: 6px; }
  .offer__service-type { font-size: 64px; color: var(--orange); margin-top: 4px; }
  .terms {
    position: absolute;
    left: 690px;
    top: 683px;
    margin: 0;
    padding: 0;
    list-style: none;
    font-family: "Open Sans", Arial, sans-serif;
    font-weight: 700;
    font-size: 16px;
    line-height: 1.3;
  }
  .terms li::before { content: "* "; }
  .expiry {
    position: absolute;
    left: 1020px;
    top: 305px;
    width: 165px;
    height: 410px;
  }
  .expiry__label {
    position: absolute;
    left: 0;
    top: 0;
    width: 50px;
    height: 410px;
    display: flex;
    align-items: center;
    justify-content: center;
  }
  .expiry__label span {
    transform: rotate(-90deg);
    white-space: nowrap;
    font-weight: 800;
    font-size: 19px;
    letter-spacing: 0.5px;
  }
  .expiry__field {
    position: absolute;
    left: 62px;
    top: 0;
    width: 103px;
    height: 410px;
  }
</style>
</head>
<body>
<main class="coupon">
  <svg class="coupon__backdrop" width="1200" height="750" viewBox="0 0 1200 750" aria-hidden="true">
    <path d="M690 0 H1200 V750 H1010 C1000 520 980 330 900 230 C840 160 730 110 690 0 Z" fill="var(--blue-dark)"/>
  </svg>

  <svg class="washer-door" width="1200" height="750" viewBox="0 0 1200 750" role="img" aria-label="Washing machine door with swirling water and soap bubbles">
    <defs>
      <radialGradient id="waterGlow" cx="0.45" cy="0.4" r="0.7">
        <stop offset="0" stop-color="var(--blue-pale)"/>
        <stop offset="1" stop-color="var(--blue-light)"/>
      </radialGradient>
    </defs>
    <circle cx="290" cy="560" r="410" fill="var(--orange)" stroke="var(--white)" stroke-width="7"/>
    <rect x="440" y="385" width="85" height="32" rx="16" fill="var(--white)"/>
    <rect x="440" y="478" width="85" height="32" rx="16" fill="var(--white)"/>
    <circle cx="290" cy="560" r="300" fill="var(--white)"/>
    <circle cx="290" cy="560" r="278" fill="url(#waterGlow)"/>
  </svg>

  <div class="website">www.sudsonseventh.com</div>

  <div class="brand">
    <span class="brand__mark"></span>
    <span class="brand__name">Suds on Seventh</span>
  </div>

  <address class="contact" style="font-style:normal">
    215 S 700W<br>
    Orem UT, 84058 USA<br>
    <span class="contact__phone">
      <svg viewBox="0 0 24 24" aria-hidden="true"><path fill="#ffffff" d="M6.6 10.8a15.1 15.1 0 0 0 6.6 6.6l2.2-2.2a1 1 0 0 1 1-.25 11.4 11.4 0 0 0 3.6.57 1 1 0 0 1 1 1V20a1 1 0 0 1-1 1A17 17 0 0 1 3 4a1 1 0 0 1 1-1h3.5a1 1 0 0 1 1 1c0 1.25.2 2.45.57 3.6a1 1 0 0 1-.25 1z"/></svg>
      801.555.0148
    </span>
  </address>

  <h1 class="offer" style="margin:0;font-weight:400">
    <span class="offer__line offer__one">One</span>
    <span class="offer__line offer__free">FREE</span>
    <span class="offer__line offer__service-name">wash-n-fold</span>
    <span class="offer__line offer__service-type">laundry service</span>
  </h1>

  <ul class="terms">
    <li>Limit one coupon per customer.</li>
    <li>Limit 50 pounds of laundry per coupon.</li>
  </ul>

  <div class="expiry">
    <div class="expiry__label"><span>THIS OFFER GOOD THROUGH</span></div>
    <svg class="expiry__field" viewBox="0 0 103 410" aria-hidden="true">
      <rect x="0" y="0" width="103" height="410" fill="var(--white)"/>
      <line x1="10" y1="40" x2="95" y2="135" stroke="var(--line-grey)" stroke-width="2"/>
      <line x1="10" y1="230" x2="95" y2="325" stroke="var(--line-grey)" stroke-width="2"/>
    </svg>
  </div>
</main>
</body>
</html>
```